Buch-/E-Book-Cover für Autobiografie
Zielgruppe
Ich bin Autor und habe soeben meine Autobiografie verfasst. Sie handelt hauptsächlich von meiner Flagfootball Karriere und meinem Weg vom American Football Fan zum Flagfootball Weltmeister.
Ich benötige ein Design für das Cover des Buches im DIN A5 Format. Es sollte sehr edel aussehen.
Buchtitel: Funkenflug
Untertitel: Eine Reise über Rasen, Regen und Rekorde bis ganz nach oben
Aufgabenstellung
Auf der Vorderseite sollte eines der mitgeschickten Bilder, der Titel, der Untertitel des Buches und mein Name stehen. Egal, welches Foto für die Vorderseite ausgewählt wird, der Football sollte jedenfalls gut erkennbar sein.
Auf der Rückseite eine Buchbeschreibung und drei kurze Statements von Testimonials.
Auf dem Buchrücken mein Name und der Buchtitel (ohne Untertitel).
Farblich sollte sich das Design an den Farben meiner Website anlehnen (Hauptfarben Gold, Weiss, Schwarz)

```html
<!DOCTYPE html>
<html lang="de">
<head>
<meta charset="utf-8">
<title>Funkenflug – Buchcover</title>
<link rel="stylesheet" href="https://fonts.googleapis.com/css2?family=Oswald:wght@300;400;700&family=Jost:wght@400&display=swap">
<style>
  :root {
    --gold: #d2b870;
    --gold-title: #c9ae6a;
    --black: #0d0d0d;
    --white: #ffffff;
    --edge: #4a4232;
  }
  * { box-sizing: border-box; margin: 0; padding: 0; }
  html, body { width: 1200px; height: 810px; overflow: hidden; background: #ffffff; }
  .cover { position: relative; width: 1200px; height: 810px; }

  .back { position: absolute; left: 0; top: 0; width: 572px; height: 810px; background: var(--gold); }
  .back-title {
    position: absolute; left: 50px; top: 40px; width: 472px;
    font: 700 96px/1 "Oswald", sans-serif; color: var(--black);
    text-align: center; letter-spacing: 1px;
  }
  .back-subtitle {
    position: absolute; left: 30px; top: 140px; width: 512px;
    font: 300 24px/30px "Oswald", sans-serif; color: var(--white);
    text-align: center; text-transform: uppercase;
  }
  .blurb {
    position: absolute; left: 49px; width: 476px;
    font: 400 14.2px/19.6px "Jost", sans-serif; color: var(--black);
  }
  .blurb-1 { top: 212px; }
  .blurb-2 { top: 349px; }
  .blurb-3 { top: 466px; }
  .testimonials { position: absolute; left: 50px; top: 527px; width: 476px; list-style: none; }
  .testimonial {
    font: 700 30px/43px "Oswald", sans-serif; font-style: italic;
    color: var(--white); text-align: center; letter-spacing: 0.5px;
  }
  .code-box { position: absolute; left: 374px; top: 690px; width: 160px; height: 90px; background: var(--white); }

  .spine {
    position: absolute; left: 571px; top: 0; width: 58px; height: 810px;
    background: var(--gold);
    border-left: 1px solid var(--edge); border-right: 1px solid var(--edge);
  }
  .spine-title, .spine-author {
    position: absolute; left: 50%; white-space: nowrap;
    transform: translate(-50%, -50%) rotate(-90deg);
  }
  .spine-title { top: 278px; font: 700 36px/1 "Oswald", sans-serif; color: var(--black); }
  .spine-author { top: 596px; font: 300 26px/1 "Oswald", sans-serif; color: var(--white); letter-spacing: 9px; }

  .front { position: absolute; left: 629px; top: 0; width: 571px; height: 810px; overflow: hidden; }
  .front-photo {
    position: absolute; inset: 0;
    background: linear-gradient(180deg, #ddd6c8 0%, #d6cdbd 38%, #a89c8c 52%, #1c1d22 62%, #111216 100%);
  }
  .front-author {
    position: absolute; left: 0; top: 26px; width: 571px;
    font: 400 38px/1 "Oswald", sans-serif; color: var(--white);
    text-align: center; letter-spacing: 14px; padding-left: 30px;
  }
  .front-title {
    position: absolute; left: 0; top: 548px; width: 571px;
    font: 700 92px/1 "Oswald", sans-serif; color: var(--gold-title);
    text-align: center; letter-spacing: 1px;
  }
  .front-subtitle {
    position: absolute; left: 0; top: 642px; width: 571px;
    font: 300 24px/30px "Oswald", sans-serif; color: var(--white);
    text-align: center; text-transform: uppercase;
  }
</style>
</head>
<body>
<main class="cover">
  <section class="back">
    <h2 class="back-title">FUNKENFLUG</h2>
    <p class="back-subtitle">Eine Reise über Rasen, Regen und Rekorde<br>bis ganz nach oben</p>
    <p class="blurb blurb-1">In meiner Autobiografie erzähle ich die spannende und einzigartige Geschichte, wie ich vom American Football Fan zum Flagfootball Weltmeister wurde. Motiviert durch das Verfolgen der Nordliga und einem zufälligen Treffen mit meinem großen Sportidol, wuchs in mir der Wunsch, selbst am Spielfeld zu stehen und Erfolge zu feiern. Doch wo sollte ich anfangen? Am besten bei null, denn ich hatte nie zuvor Flagfootball gespielt.</p>
    <p class="blurb blurb-2">Auf unterhaltsame und lustige Weise tauche ich in den Beginn meiner Reise in den frühen 2000er Jahren ein. Das Ziel fest vor Augen, gründete ich den ersten steirischen Flagfootball Verein und startete meinen Weg der mich bis zur Weltmeisterschaft führte, wo ich als Quarterback mit der österreichischen Nationalmannschaft den Titel holte.</p>
    <p class="blurb blurb-3">Begleite mich durch meine Geschichte und erlebe mit mir Höhen und Tiefen, Erfolge und Rückschläge und meinen größten Triumph.</p>
    <ul class="testimonials">
      <li class="testimonial">“GO FOR GOLD, GO FOR GOLD”</li>
      <li class="testimonial">“GO FOR GOLD, GO FOR GOLD”</li>
      <li class="testimonial">“GO FOR GOLD, GO FOR GOLD”</li>
    </ul>
    <div class="code-box"></div>
  </section>

  <section class="spine">
    <span class="spine-title">FUNKENFLUG</span>
    <span class="spine-author">KONRAD WESSLING</span>
  </section>

  <section class="front">
    <div class="front-photo" role="img" aria-label="Porträtfoto des Autors in schwarzem T-Shirt vor heller, beiger Wand"></div>
    <p class="front-author">KONRAD WESSLING</p>
    <h1 class="front-title">FUNKENFLUG</h1>
    <p class="front-subtitle">Eine Reise über Rasen, Regen und Rekorde<br>bis ganz nach oben</p>
  </section>
</main>
</body>
</html>
```